I am looking for help designing my new business cards. I would like rounded edges and a raised logo on the back of the card. I have 2 Logos. One with a boat in it and one without. I'd like the one on the back to be the one that includes the boat and just the name on the front. I have included multiple formats of my logo. Please let me know if you need anymore.

Target Market(s)

Potential buyers and other sales brokers

Industry/Entity Type

Sales - Yacht / Boat Sales

Contact Information for Business Card

Id liike the front to include just the business name portion of the logo along with my name (Corwin Dalby), phone number (555.318.6027), website address (www.dalbymarineco.example) and not my physical address but just "Charleston, SC". The back should include my full logo that has the boat included. This portion I'd prefer raised amd take up the majority of the space there. Thanks!!

Colors
0054AA
0677BA
7BADD7
CADEEF
E8F1F8
0094D4
00A9DD
6FCCEA
C7EBF8
E9F6FB

Requirements
Must have
• Double sided
Nice to have
• My email address: Corwin@dalbymarineco.example The NMTG logo somewhere small on the front of the card
Should not have
• My full address, prefer only "Charleston, SC"

```html
<!DOCTYPE html>
<html lang="en">
<head>
<meta charset="utf-8">
<title>Dalby Marine Co — Business Card</title>
<link href="https://fonts.googleapis.com/css2?family=Arimo:wght@400;700&display=swap" rel="stylesheet">
<style>
  :root {
    --backdrop: #e6e9ec;
    --brand-blue: #0677BA;
    --brand-sky: #0094D4;
    --brand-navy: #10295c;
    --boat-tint: #4a9fd4;
    --ghost-tint: #e8edf3;
    --card-white: #ffffff;
    --text-blue: #0677BA;
  }
  * { box-sizing: border-box; margin: 0; padding: 0; }
  html, body {
    width: 1200px; height: 805px; overflow: hidden;
    background: var(--backdrop);
    font-family: "Arimo", Arial, sans-serif;
  }
  .stage { position: relative; width: 1200px; height: 805px; }

  .card { position: absolute; border-radius: 22px; overflow: hidden; }

  /* Back of card */
  .card-back {
    left: 336px; top: 78px; width: 512px; height: 294px;
    background: var(--brand-blue);
  }
  .card-back .boat-mark {
    position: absolute; left: 120px; top: 20px; width: 300px; height: 145px;
    border-radius: 40px 40px 60px 60px;
    background: radial-gradient(ellipse at center, var(--boat-tint) 0%, var(--brand-blue) 75%);
  }
  .card-back .brand-name {
    position: absolute; left: 0; right: 0; top: 166px;
    text-align: center; color: var(--card-white); font-weight: 700;
  }
  .card-back .brand-name .primary { display: block; font-size: 62px; line-height: 64px; letter-spacing: 8px; }
  .card-back .brand-name .secondary { display: block; font-size: 22px; line-height: 30px; letter-spacing: 3px; }

  /* Front of card */
  .card-front {
    left: 341px; top: 423px; width: 502px; height: 287px;
    background: var(--card-white);
  }
  .card-front .brand-name {
    position: absolute; left: 8px; top: 30px; width: 220px;
    text-align: center; color: var(--brand-navy); font-weight: 700;
  }
  .card-front .brand-name .primary { display: block; font-size: 40px; line-height: 40px; letter-spacing: 5px; }
  .card-front .brand-name .secondary { display: block; font-size: 14px; line-height: 18px; letter-spacing: 2px; }
  .card-front .ghost-boat {
    position: absolute; left: 44px; top: 150px; width: 430px; height: 125px;
    border-radius: 50px 90px 90px 70px;
    background: linear-gradient(180deg, rgba(232,237,243,0) 0%, var(--ghost-tint) 55%, rgba(232,237,243,0.2) 100%);
  }
  .card-front .swoosh { position: absolute; left: 0; top: 0; }
  .contact {
    position: absolute; left: 134px; width: 310px; text-align: center;
  }
  .contact-name { top: 141px; font-size: 27px; font-weight: 700; color: var(--brand-navy); letter-spacing: 0.5px; }
  .contact-phone {
    top: 176px; font-size: 22px; color: var(--text-blue);
    display: flex; align-items: center; justify-content: center; gap: 4px;
  }
  .contact-web { top: 229px; font-size: 17px; color: var(--brand-navy); }
  .contact-city { top: 255px; font-size: 17px; color: var(--text-blue); }
</style>
</head>
<body>
<main class="stage">

  <section class="card card-back" aria-label="Card back">
    <div class="boat-mark" role="img" aria-label="Raised boat illustration of the company logo"></div>
    <div class="brand-name">
      <span class="primary">DALBY</span>
      <span class="secondary">MARINE CO</span>
    </div>
  </section>

  <section class="card card-front" aria-label="Card front">
    <div class="ghost-boat" role="img" aria-label="Faint boat illustration in the background"></div>
    <svg class="swoosh" width="502" height="287" viewBox="0 0 502 287" aria-hidden="true">
      <path d="M0 165 C 120 150, 170 110, 260 70 C 340 35, 420 28, 480 38 C 420 36, 345 50, 270 90 C 180 138, 120 168, 0 172 Z" fill="var(--brand-sky)"/>
    </svg>
    <div class="brand-name">
      <span class="primary">DALBY</span>
      <span class="secondary">MARINE CO</span>
    </div>
    <div class="contact contact-name">CORWIN DALBY</div>
    <div class="contact contact-phone">
      <svg width="20" height="20" viewBox="0 0 20 20" aria-hidden="true">
        <circle cx="10" cy="10" r="10" fill="var(--brand-navy)"/>
        <path d="M7 5.5 L8.6 5.2 L9.4 7.6 L8.4 8.4 C8.9 9.7 10 10.9 11.4 11.5 L12.2 10.5 L14.6 11.3 L14.3 12.9 C13.9 13.9 12.8 14.2 11.8 13.9 C9 13 6.8 10.8 6 8 C5.7 7 6 5.9 7 5.5 Z" fill="var(--card-white)"/>
      </svg>
      <span>555.318.6027</span>
    </div>
    <div class="contact contact-web">www.dalbymarineco.example</div>
    <div class="contact contact-city">Port Ellis,GA</div>
  </section>

</main>
</body>
</html>
```